I am a highly experienced private practice psychotherapist serving high end clientele in the Wall Street area of New York City. I need electronic letterhead (that can also be printed) to use for bills, receipts, and correspondences.

My clients are very high end and are used to elegance and wealth. The letterhead should contain the following information: Marian T. Holcombe, LCSW 72 Pellham Street, Suite 2561 New York, NY 10087 Phone : (917) 555-3194 email: therapy@marianholcombelcsw.example website: www.marianholcombelcsw.example

Thank you for your designs. Please be advised that the letterhead will be used for bills/invoices; professional letters to other mental health professionals and doctors, as well as to attorneys. It needs to be highly professional in the same way that a law firm has professional and elegant letterhead, raher than whimsical or with spa designers. My letters end up as official documents.

```html
<!DOCTYPE html>
<html lang="en">
<head>
<meta charset="utf-8">
<title>Marian T. Holcombe, LCSW — Letterhead</title>
<link rel="stylesheet" href="https://fonts.googleapis.com/css2?family=Crimson+Text:wght@400;600&display=swap">
<style>
  :root {
    --accent-blue: #27aae1;
    --accent-grey: #bcbec0;
    --ink: #111111;
    --paper: #ffffff;
    --rule: #1a1a1a;
  }
  * { margin: 0; padding: 0; box-sizing: border-box; }
  html, body {
    width: 933px;
    height: 1200px;
    overflow: hidden;
    background: var(--paper);
  }
  .letterhead {
    position: relative;
    width: 933px;
    height: 1200px;
    background: var(--paper);
    font-family: "Crimson Text", Georgia, serif;
    color: var(--ink);
    overflow: hidden;
  }
  .corner-motif {
    position: absolute;
    display: block;
  }
  .corner-motif--top { left: 0; top: 0; }
  .corner-motif--bottom { left: 743px; top: 1052px; }

  .sender {
    position: absolute;
    left: 653px;
    top: 32px;
  }
  .sender__name {
    font-size: 19px;
    font-weight: 400;
    letter-spacing: 0.6px;
    text-transform: uppercase;
    line-height: 22px;
  }
  .sender__phone {
    font-size: 16px;
    line-height: 22px;
  }
  .label { color: var(--accent-blue); }

  .footer-rule {
    position: absolute;
    left: 62px;
    top: 1100px;
    width: 633px;
    height: 0;
    border-top: 1.5px solid var(--rule);
  }
  .contact {
    position: absolute;
    top: 1108px;
    font-size: 16px;
    line-height: 21px;
  }
  .contact--address {
    left: 75px;
    display: grid;
    grid-template-columns: auto auto;
    column-gap: 4px;
  }
  .contact--online { left: 396px; }
</style>
</head>
<body>
  <main class="letterhead">
    <svg class="corner-motif corner-motif--top" width="263" height="308" viewBox="0 0 263 308" role="img" aria-label="Geometric tile motif in blue and grey">
      <defs>
        <linearGradient id="motif-top" x1="0" y1="0" x2="1" y2="1">
          <stop offset="0" stop-color="#bcbec0"/>
          <stop offset="0.55" stop-color="#7fc2e3"/>
          <stop offset="1" stop-color="#27aae1"/>
        </linearGradient>
      </defs>
      <polygon points="0,0 263,0 263,308 0,226" fill="url(#motif-top)"/>
    </svg>

    <header class="sender">
      <h1 class="sender__name">Marian T. Holcombe</h1>
      <p class="sender__phone"><span class="label">Phone :</span> (917) 555-3194</p>
    </header>

    <div class="footer-rule"></div>

    <address class="contact contact--address" style="font-style: normal;">
      <span class="label">Address:</span>
      <span>LCSW 72 Pellham Street,<br>Suite 2561 New York,<br>NY 10087</span>
    </address>

    <address class="contact contact--online" style="font-style: normal;">
      <p><span class="label">Email:</span> therapy@marianholcombelcsw.example</p>
      <p><span class="label">Website:</span> www.marianholcombelcsw.example</p>
    </address>

    <svg class="corner-motif corner-motif--bottom" width="172" height="148" viewBox="0 0 172 148" role="img" aria-label="Geometric tile motif in blue and grey">
      <defs>
        <linearGradient id="motif-bottom" x1="0" y1="0" x2="1" y2="1">
          <stop offset="0" stop-color="#27aae1"/>
          <stop offset="0.5" stop-color="#7fc2e3"/>
          <stop offset="1" stop-color="#bcbec0"/>
        </linearGradient>
      </defs>
      <polygon points="0,0 172,51 172,148 0,148" fill="url(#motif-bottom)"/>
    </svg>
  </main>
</body>
</html>
```